Fennick Medical - Flyer

We are a full service pharmacy that specializes in diabetic testing and medications. We research the patient's insurance to maximize their insurance benefit and then deliver the medications monthly directly to the patient's doorstep, for free! We save the patient, time and money every month.
We would love a flyer that we can distribute to Doctor's offices and patients that sum up our pharmacy. Emphasis on saving money, time, and getting the best quality supplies by maximizing their insurance. We want it to be eye catching, clean, and professional.
You can use our logo or feel free to make your own design.
diabetic patients wanting to save money
Insurance

```html
<!DOCTYPE html>
<html lang="en">
<head>
<meta charset="utf-8">
<title>Fennick Medical – Flyer</title>
<link rel="stylesheet" href="https://fonts.googleapis.com/css2?family=Arimo:wght@400;700&display=swap">
<style>
  :root {
    --stage: #e9ecee;
    --sky-top: #cfeaf2;
    --sky-mid: #eef8fb;
    --sky-low: #dcedf3;
    --green: #7dbb2a;
    --green-light: #c3e294;
    --ink: #1c1c1c;
    --logo-grey: #3b3b3b;
    --url-green: #2f5d3a;
    --white: #ffffff;
    --pulse: 95,183,192;
    --heart: 226,54,43;
    --skin: 217,165,138;
    --suit: 42,42,42;
  }
  * { box-sizing: border-box; margin: 0; padding: 0; }
  html, body { width: 1200px; height: 1019px; overflow: hidden; }
  body {
    background: var(--stage);
    font-family: "Arimo", Arial, sans-serif;
    color: var(--ink);
    position: relative;
  }
  .flyer {
    position: absolute;
    top: 193px;
    width: 512px;
    height: 663px;
    overflow: hidden;
    background:
      radial-gradient(circle at 30% 25%, rgba(255,255,255,.9) 0, rgba(255,255,255,0) 45%),
      radial-gradient(circle at 75% 60%, rgba(255,255,255,.8) 0, rgba(255,255,255,0) 40%),
      linear-gradient(180deg, var(--sky-top) 0%, var(--sky-mid) 45%, var(--sky-low) 100%);
    box-shadow: 0 6px 18px rgba(0,0,0,.18);
  }
  .flyer--front { left: 58px; }
  .flyer--back { left: 617px; }

  .wave { position: absolute; left: 0; bottom: 0; width: 512px; height: 260px; }

  .brand { position: absolute; display: flex; align-items: center; gap: 12px; color: var(--logo-grey); font-weight: 400; }
  .brand__dot { width: 22px; height: 22px; border-radius: 50%; background: var(--green); flex: none; }
  .brand__name { line-height: 1; }
  .brand__word { display: block; }
  .brand__word--sub { letter-spacing: .42em; }

  .flyer--front .brand { left: 112px; top: 40px; }
  .flyer--front .brand__word--main { font-size: 46px; }
  .flyer--front .brand__word--sub { font-size: 21px; margin-top: 4px; }
  .flyer--back .brand { left: 258px; top: 362px; }
  .flyer--back .brand__word--main { font-size: 36px; }
  .flyer--back .brand__word--sub { font-size: 16px; margin-top: 3px; }

  .art { position: absolute; }
  .art--pulse {
    left: 74px; top: 138px; width: 400px; height: 188px;
    background:
      radial-gradient(circle at 46% 50%, rgba(var(--heart),.28) 0, rgba(var(--heart),0) 14%),
      radial-gradient(ellipse 50% 46% at 48% 50%, rgba(var(--pulse),.22) 0, rgba(var(--pulse),0) 100%);
  }
  .art--family {
    left: 118px; top: 453px; width: 248px; height: 157px;
    background: linear-gradient(180deg, rgba(var(--skin),.2) 0%, rgba(var(--skin),.55) 100%);
    border-radius: 70px 70px 0 0;
  }
  .art--celebrate {
    left: 64px; top: 310px; width: 175px; height: 193px;
    background: radial-gradient(ellipse 45% 50% at 50% 50%, rgba(var(--suit),.45) 0, rgba(var(--suit),0) 100%);
  }
  .art--heart {
    left: 22px; top: 577px; width: 72px; height: 72px;
    background: radial-gradient(circle at 50% 45%, rgba(var(--heart),.7) 0, rgba(var(--heart),0) 70%);
  }

  .tagline {
    position: absolute; left: 0; top: 356px; width: 100%;
    text-align: center; font-size: 18.5px; line-height: 24px;
  }
  .web { position: absolute; font-size: 17px; }
  .flyer--front .web { left: 0; width: 100%; text-align: center; top: 629px; color: var(--white); }
  .flyer--back .web { right: 48px; top: 549px; font-size: 15px; color: var(--url-green); }

  .about { position: absolute; left: 44px; top: 72px; width: 430px; font-size: 17.5px; line-height: 22px; }
  .about p + p { margin-top: 22px; }

  .address {
    position: absolute; left: 260px; top: 455px; width: 212px; height: 71px;
    background: rgba(196,228,160,.55);
    color: rgba(125,187,42,.6); font-size: 18px;
    display: flex; align-items: center; justify-content: center;
  }
  .call {
    position: absolute; left: 127px; top: 623px;
    color: var(--white); font-weight: 700; font-size: 27px; line-height: 1;
  }
</style>
</head>
<body>

<section class="flyer flyer--front">
  <svg class="wave" viewBox="0 0 512 260" preserveAspectRatio="none" aria-hidden="true">
    <path d="M0 180 C 200 170 380 110 512 65 L512 260 L0 260 Z" fill="var(--green-light)" opacity=".8"/>
    <path d="M0 177 C 150 205 350 200 512 160 L512 260 L0 260 Z" fill="var(--green)"/>
  </svg>

  <div class="brand">
    <span class="brand__dot"></span>
    <span class="brand__name">
      <span class="brand__word brand__word--main">FENNICK</span>
      <span class="brand__word brand__word--sub">MEDICAL</span>
    </span>
  </div>

  <div class="art art--pulse" role="img" aria-label="Heartbeat line shaped into a heart, with a red heart held by a green hand"></div>

  <p class="tagline">Saving Your Money, Time and getting<br>the best quality supplies by maximizing<br>their Insurance.</p>

  <div class="art art--family" role="img" aria-label="Photo of four fingers drawn as a smiling family"></div>

  <p class="web">www.fennickmedical.com</p>
</section>

<section class="flyer flyer--back">
  <svg class="wave" viewBox="0 0 512 260" preserveAspectRatio="none" aria-hidden="true">
    <path d="M0 110 C 140 190 330 195 512 140 L512 260 L0 260 Z" fill="var(--green-light)" opacity=".8"/>
    <path d="M0 195 C 170 225 380 205 512 172 L512 260 L0 260 Z" fill="var(--green)"/>
  </svg>

  <div class="about">
    <p>We are a full service pharmacy that specializes in<br>diabetic testing and medications.</p>
    <p>We research the patient's insurance to maximize their<br>insurance benefit and then deliver the medications<br>monthly directly to the patient's doorstep, for free!</p>
    <p>We save the patient, time and money every month.</p>
  </div>

  <div class="art art--celebrate" role="img" aria-label="Silhouette of a man in a suit with arms raised in celebration"></div>

  <div class="brand">
    <span class="brand__dot"></span>
    <span class="brand__name">
      <span class="brand__word brand__word--main">FENNICK</span>
      <span class="brand__word brand__word--sub">MEDICAL</span>
    </span>
  </div>

  <div class="address">Address</div>
  <p class="web">www.fennickmedical.com</p>

  <div class="art art--heart" role="img" aria-label="Red heart held in a green hand"></div>
  <p class="call">Call Us Now 55501234</p>
</section>

</body>
</html>
```